Tilda Tinkerwire, An IT Company Has New Logo, Need Fresh Business Cards

IT company is called Tilda Tinkerwire and is displayed nicely with the new logo from here on pitchloft. Would like a fresh business card look that encompasses the idea that we want clients to Cherish Every Gadget. I love the use of circuitry with hearts as endpoints and x's and o's. It needs to have room for my certification logos of which there are 4 and a BRJ Alumni log. I am attaching my current card to illustrate how it has always captured attention, but that was in the early stages of business when I was doing more residential work. I am focused on businesses now, so a level of professionalism is necessary. I would also like the card to lend itself well to additional stationary, email signature, ticketing template for my workboard, etc. For the time being, I need the card for an upcoming conference so that work will come later. Color scheme should be that of the new logo. Thank you and I look forward to the designs.

Target Market(s)

Businesses looking for IT services.

Industry/Entity Type

Information Technology

Contact Information for Business Card

See above

Requirements
Must have
• New logo colors and a warm feel. Possibly a tad feminine as I am female, but appealing to males.
Nice to have
• I would like techy, but no too much so. I like friendly and connecting feels. People LOVED my old card and called me because it gave them a warm feeling.

```html
<!DOCTYPE html>
<html lang="en">
<head>
<meta charset="utf-8">
<title>Tilda Tinkerwire – Business Card</title>
<link href="https://fonts.googleapis.com/css2?family=Cabin:ital,wght@0,400;0,500;1,700&display=swap" rel="stylesheet">
<style>
  :root {
    --page-bg: #eceef1;
    --card-bg: #ffffff;
    --sky: #5fb3e0;
    --lime: #a9cf4a;
    --ink: #2b2b2b;
    --rule: #9ccfe9;
    --trace-a: #e6f1f8;
    --trace-b: #f0f6e4;
  }
  * { margin: 0; padding: 0; box-sizing: border-box; }
  html, body {
    width: 1200px; height: 800px; overflow: hidden;
    background: var(--page-bg);
    font-family: "Cabin", sans-serif;
  }
  .canvas {
    width: 1200px; height: 800px;
    display: flex; align-items: center; justify-content: center;
  }
  .business-card {
    position: relative;
    width: 1000px; height: 572px;
    background: var(--card-bg);
    box-shadow: 0 6px 24px rgba(0,0,0,0.12);
    overflow: hidden;
  }
  .circuit-backdrop {
    position: absolute; left: 0; top: 90px;
    width: 640px; height: 482px;
    background: linear-gradient(135deg, var(--trace-a), var(--trace-b) 60%, rgba(255,255,255,0) 100%);
    opacity: 0.7;
  }
  .brand {
    position: absolute; left: 40px; top: 190px;
    display: flex; flex-direction: column; align-items: center;
  }
  .brand-mark {
    width: 26px; height: 26px; border-radius: 50%;
    background: var(--sky); margin-bottom: 14px;
  }
  .brand-name {
    font-size: 44px; font-weight: 500; color: var(--sky);
    letter-spacing: 0.5px;
  }
  .brand-tagline {
    font-size: 15px; color: var(--sky);
    letter-spacing: 5px; text-transform: uppercase; margin-top: 2px;
  }
  .services {
    position: absolute; right: 44px; top: 36px; text-align: right;
  }
  .services-title {
    font-size: 36px; font-style: italic; font-weight: 700;
    color: var(--sky); letter-spacing: 1px; text-transform: uppercase;
    padding-bottom: 6px; border-bottom: 2px solid var(--lime);
  }
  .services-list { font-size: 25px; color: var(--ink); margin-top: 8px; }
  .call-block {
    position: absolute; right: 44px; top: 395px; text-align: right;
  }
  .call-prompt { font-size: 25px; color: var(--ink); }
  .call-phone { font-size: 42px; color: var(--sky); letter-spacing: 1px; }
  .contact-rule {
    position: absolute; left: 220px; right: 36px; top: 494px;
    border-top: 2px solid var(--rule);
  }
  .contact-line {
    position: absolute; right: 36px; top: 505px;
    font-size: 23px; color: var(--ink);
  }
  .contact-line .divider { margin: 0 8px; }
</style>
</head>
<body>
<main class="canvas">
  <section class="business-card">
    <div class="circuit-backdrop" role="img" aria-label="Faint pastel circuit-trace pattern with round endpoints"></div>

    <div class="brand">
      <span class="brand-mark"></span>
      <span class="brand-name">Tilda Tinkerwire</span>
      <span class="brand-tagline">Cherish Every Gadget</span>
    </div>

    <div class="services">
      <h1 class="services-title">Computer Care &amp; Repair</h1>
      <p class="services-list">Desktops laptops tablets</p>
    </div>

    <div class="call-block">
      <p class="call-prompt">Call Tilda!</p>
      <p class="call-phone">470- 555- 0142</p>
    </div>

    <div class="contact-rule"></div>
    <p class="contact-line">tilda.tinkerwire@mailbox.com<span class="divider">|</span>www.tilda-tinkerwire.com</p>
  </section>
</main>
</body>
</html>
```